Infografiken für Rechtsfirma
Zielgruppe
Wir sind eine Rechtsfirma, welche sich mit dem europäischen Recht beschäftigt. Wir bieten Insolvenzen in unterschiedlichen Ländern an. Weiter beraten wir hinsichtlich des Vermögensschutzes. Wir helfen dabei, Vermögenswerte zu sichern. Für unseren Bereich Vermögensschutz benötigen wir eine Grafik, welche die Vorteile unseres Produkts direkt auf einen Blick erkennen lässt. Hierzu habe ich eine Grafik eines großen Mobilfunkherstellers beigefügt. Im gleichen Designe möchten wir diese Grafik haben.
Aufgabenstellung
Ich habe eine PDF-Datei (Vermögensschutz) beigefügt, aus welcher sich die Keyfacts ergeben. Diese müssen grafisch aufbereitet werden.

```html
<!DOCTYPE html>
<html lang="de">
<head>
<meta charset="utf-8">
<title>Vermögensschutz – Legal und rechtssicher</title>
<link href="https://fonts.googleapis.com/css2?family=Oswald:wght@400;500;600&display=swap" rel="stylesheet">
<style>
  :root{
    --ink:#1b2c33;
    --shield:#0f2a31;
    --bg-center:#ffffff;
    --bg-edge:#e4ecef;
    --line:#1b2c33;
    --white:#ffffff;
  }
  *{margin:0;padding:0;box-sizing:border-box}
  html,body{width:1200px;height:747px;overflow:hidden}
  body{
    font-family:'Oswald',sans-serif;
    color:var(--ink);
    background:radial-gradient(ellipse at 50% 50%,var(--bg-center) 0%,#f4f8f9 45%,var(--bg-edge) 100%);
    position:relative;
  }
  .connectors{position:absolute;left:0;top:0}
  .shield-text{
    position:absolute;left:516px;top:352px;width:170px;text-align:center;color:var(--white);
    text-transform:uppercase;
  }
  .shield-text .kicker{font-size:13px;font-weight:400;letter-spacing:.3px;display:block;margin-bottom:4px}
  .shield-text .claim{font-size:20px;font-weight:500;line-height:1.1;display:block}
  .icon{position:absolute}
  .benefit{position:absolute;text-transform:uppercase}
  .benefit h2{font-size:16px;font-weight:500;line-height:1.15;letter-spacing:.2px}
  .benefit p{font-size:11px;font-weight:500;line-height:1.25}
  .benefit .value{font-size:50px;font-weight:500;line-height:1;margin-top:4px;display:block}
  .benefit ul{list-style:none;margin-top:3px}
  .benefit li{font-size:8.5px;font-weight:400;line-height:1.55;padding-left:10px;position:relative}
  .benefit li::before{content:"";position:absolute;left:0;top:4.5px;width:4px;height:4px;border-radius:50%;background:var(--ink)}
</style>
</head>
<body>
  <svg class="connectors" width="1200" height="747" viewBox="0 0 1200 747" aria-hidden="true">
    <g stroke="var(--line)" stroke-width="2">
      <line x1="403" y1="190" x2="530" y2="317"/>
      <line x1="601" y1="219" x2="601" y2="289"/>
      <line x1="786" y1="204" x2="671" y2="317"/>
      <line x1="429" y1="389" x2="499" y2="389"/>
      <line x1="701" y1="389" x2="771" y2="389"/>
      <line x1="408" y1="578" x2="527" y2="461"/>
      <line x1="601" y1="499" x2="601" y2="567"/>
      <line x1="675" y1="462" x2="777" y2="567"/>
    </g>
    <polygon points="516,332 540,322 662,322 686,332 686,445 601,516 516,445" fill="var(--shield)"/>
  </svg>

  <div class="shield-text">
    <span class="kicker">Vermögensschutz</span>
    <span class="claim">Legal und<br>rechtssicher</span>
  </div>

  <!-- Anonymität -->
  <div class="icon" role="img" aria-label="Symbol: anonyme Person mit Fragezeichen" style="left:149px;top:106px;width:106px;height:106px;border-radius:50%;background:radial-gradient(circle at 40% 35%,#1fa37a,#0e4a52 75%)"></div>
  <div class="benefit" style="left:284px;top:104px">
    <h2>Anonymity</h2>
    <p>Keine Rückschlüsse<br>auf Sie möglich</p>
    <span class="value">100%</span>
  </div>

  <!-- Sicherung von Vermögenswerten -->
  <div class="icon" role="img" aria-label="Symbol: Goldbarren, Dokument, Münze und Haus" style="left:476px;top:96px;width:112px;height:118px;border-radius:10px;background:linear-gradient(160deg,#f8b62d,#f07f1e 55%,#e9512a)"></div>
  <div class="benefit" style="left:587px;top:102px">
    <h2>Sicherung von<br>Vermögenswerten</h2>
    <ul>
      <li>Immobilien</li>
      <li>Barvermögen</li>
      <li>Kryptowährung</li>
      <li>Firmenanteile</li>
      <li>Auto/Boot/Flugzeug/ Uhren</li>
    </ul>
  </div>

  <!-- Wegzugsbesteuerung -->
  <div class="icon" role="img" aria-label="Symbol: Steuerdokument mit Geldschein" style="left:794px;top:96px;width:80px;height:86px;border-radius:6px;background:linear-gradient(150deg,#f3c13a,#e25b4b 45%,#6fbf73)"></div>
  <div class="benefit" style="left:902px;top:104px">
    <h2>Wegzugsbesteuerung<br>Freiheit</h2>
    <span class="value">0%</span>
  </div>

  <!-- Grunderwerbssteuer -->
  <div class="icon" role="img" aria-label="Symbol: Haus mit Prozentzeichen" style="left:147px;top:351px;width:103px;height:103px;border-radius:10px;background:linear-gradient(160deg,#e2574c,#f6d66a 55%,#52b788)"></div>
  <div class="benefit" style="left:270px;top:369px">
    <h2>Grunderwerbssteuer<br>freie Einbringung</h2>
    <span class="value">0%</span>
  </div>

  <!-- Erbschaftssteuer -->
  <div class="icon" role="img" aria-label="Symbol: Vermögensübertragung zwischen zwei Personen" style="left:790px;top:338px;width:98px;height:93px;border-radius:10px;background:linear-gradient(150deg,#f7c948,#f28a3c 45%,#3fa66a)"></div>
  <div class="benefit" style="left:913px;top:344px">
    <h2>Erbschaftssteuer</h2>
    <span class="value" style="font-size:54px">0%</span>
  </div>

  <!-- Steueroptimierung -->
  <div class="icon" role="img" aria-label="Symbol: Dokumente mit Münzstapel" style="left:153px;top:578px;width:91px;height:79px;border-radius:8px;background:linear-gradient(150deg,#cfe0ea,#f2b441 60%,#2d4f5e)"></div>
  <div class="benefit" style="left:274px;top:590px">
    <h2>Steueroptimierung<br>für das laufende<br>Einkommen</h2>
  </div>

  <!-- Schutz vor Ansprüchen Dritter -->
  <div class="icon" role="img" aria-label="Symbol: Netzwerk verbundener Personen" style="left:474px;top:572px;width:88px;height:86px;border-radius:50%;background:radial-gradient(circle,#f4a259,#4aa3c9 60%,#2f5d6e)"></div>
  <div class="benefit" style="left:567px;top:606px">
    <h2>Schutz vor<br>Ansprüchen Dritter</h2>
    <ul>
      <li>Bank Finanzamt Bürgschaften</li>
      <li>Klage Sozialversicherung</li>
    </ul>
  </div>

  <!-- Insolvenzsicher -->
  <div class="icon" role="img" aria-label="Symbol: Tresor mit Sperrzeichen" style="left:790px;top:567px;width:100px;height:96px;border-radius:8px;background:linear-gradient(150deg,#e94b4b,#f5c242 40%,#3d5a66)"></div>
  <div class="benefit" style="left:907px;top:574px">
    <h2>Insolvenz sicher<br>kein Zugriff vom<br>Insolvenzverwalter</h2>
    <span class="value" style="margin-top:0">100%</span>
  </div>
</body>
</html>
```